'WILD' eye catching Business Card Design / Logo for production company / TV host / adventurer

Hi there,

We are looking for a 'WILD' and exciting logo and double sided business card for our business "Red Kettle Studios".

Corwin Baxley is an international television host, adventurer, author and inspirational public speaker.

We want to project Corwin's talents onto his business card.

We are looking for a business card design that can carry over onto letter heads, emails etc. We want a design that is 'WILD', different and exciting.

Feel free to check out Corwin's web site: www.redkettlestudios.co.nz to get a better understanding what he is about.

Please feel free to go completely 'WILD' on this project as we want something different with lots of WOW factors.

Thank you so much and we look forward to your designs.

We have a feeling that there will be many more designs in the near future.

Best regards,

the production team

We have added another task to the list.

If the winning designer can also provide us with a matching letterhead and email signature based on the same style of design as the business card.

Target Market(s)

People with passion.

Industry/Entity Type

Business

Requirements
Must have
• Red Kettle Studios
Corwin Baxley
42 Fernhill Lane
Ashbury 7388
New Zealand

Phone +64-(0)3-5027 416
Cell +64-(0)274-861 052

email: redkettlenz@mailbox-example.nz
www.redkettlestuios.co.nz
Nice to have
• A feature made out of the name 'Red Kettle Studios'.

Corwin Baxley's name reasonably obvious.

All other details (except web site) can be quite small.

```html
<!DOCTYPE html>
<html lang="en">
<head>
<meta charset="utf-8">
<title>Red Kettle Studios – Business Card</title>
<link rel="stylesheet" href="https://fonts.googleapis.com/css2?family=Bangers&family=Grandstander:wght@700;800&display=swap">
<style>
  :root {
    --bg-deep: #b8460c;
    --bg-mid: #e07a16;
    --bg-light: #f3b531;
    --glow: #fff27a;
    --brand: #a3220f;
    --link-red: #e0300f;
    --link-outline: #3a0c02;
    --name-green: #6ee51a;
    --name-dark: #0d2a04;
    --ink: #140a03;
  }
  * { margin: 0; padding: 0; box-sizing: border-box; }
  html, body {
    width: 720px;
    height: 1200px;
    overflow: hidden;
    background: var(--bg-deep);
  }
  .card {
    position: relative;
    width: 720px;
    height: 1200px;
    overflow: hidden;
    text-align: center;
  }
  .card__texture {
    position: absolute;
    inset: 0;
    background:
      radial-gradient(circle at 50% 56%, var(--glow) 0%, rgba(255,230,90,0.85) 12%, rgba(243,181,49,0.55) 28%, rgba(224,122,22,0) 50%),
      radial-gradient(ellipse at 50% 22%, rgba(255,214,90,0.55) 0%, rgba(255,214,90,0) 45%),
      radial-gradient(ellipse at 50% 50%, var(--bg-mid) 30%, var(--bg-deep) 100%);
  }
  .card__content { position: relative; }

  .brand {
    position: absolute;
    top: 70px;
    left: 0;
    right: 0;
    font-family: "Grandstander", cursive;
    font-weight: 800;
    font-size: 74px;
    line-height: 1.05;
    color: var(--brand);
  }

  .web-line {
    position: absolute;
    left: 0;
    right: 0;
    font-family: "Bangers", cursive;
    font-style: italic;
    font-size: 44px;
    letter-spacing: 1px;
    color: var(--link-red);
    -webkit-text-stroke: 2px var(--link-outline);
    text-shadow: 0 3px 4px rgba(0,0,0,0.45);
  }
  .web-line--site { top: 362px; }
  .web-line--email { top: 456px; font-size: 36px; }

  .host-name {
    position: absolute;
    top: 632px;
    left: 0;
    right: 0;
    font-family: "Bangers", cursive;
    font-style: italic;
    font-size: 86px;
    letter-spacing: 2px;
    color: var(--name-green);
    -webkit-text-stroke: 3px var(--name-dark);
    text-shadow: 6px 6px 0 var(--name-dark), 0 0 18px rgba(0,0,0,0.5);
  }

  .address {
    position: absolute;
    top: 800px;
    left: 0;
    right: 0;
    font-family: "Grandstander", cursive;
    font-weight: 700;
    font-size: 50px;
    line-height: 64px;
    color: var(--ink);
    font-style: normal;
  }

  .contact {
    position: absolute;
    top: 1020px;
    left: 0;
    right: 0;
    font-family: "Grandstander", cursive;
    font-weight: 700;
    font-size: 42px;
    line-height: 76px;
    color: var(--ink);
    list-style: none;
  }
</style>
</head>
<body>
  <main class="card">
    <div class="card__texture" role="img" aria-label="Orange grunge texture with faint tribal ornaments and a glowing sun motif in the centre"></div>
    <div class="card__content">
      <h1 class="brand">Red Kettle<br>Studios</h1>
      <p class="web-line web-line--site">REDKETTLESTUIOS.CO.NZ</p>
      <p class="web-line web-line--email">REDKETTLENZ@MAILBOX-EXAMPLE.NZ</p>
      <h2 class="host-name">CORWIN BAXLEY</h2>
      <address class="address">
        42 Fernhill Lane<br>
        Ashbury 7388<br>
        New Zealand
      </address>
      <ul class="contact">
        <li>Phone +64-(0)3-5027 416</li>
        <li>Cell +64-(0)274-861 052</li>
      </ul>
    </div>
  </main>
</body>
</html>
```